依頼詳細
アルコール除菌ジェルのラベルのデザインをお願い致します
記載項目
サイズはW110mm×H154mm
ラミネート貼り
希望イメージ
シンプル 複雑
単色 カラフル
暗い 明るい
日常 高級
遊び心 厳粛
未来的 伝統的
女性的 男性的
希望する色
緑系
納品ファイル
• イラストレーター形式 (.ai)
補足説明
実際の現在のデザイン(他社)を添付致します。
添付のデザインのOEM製品になり弊社自社品となります
雰囲気を全然違うようにしてください
業務用です
添付の画像にありますQELTは必要ございません
また発売元は弊社で製造元は別な会社で記載頂くと思います
宜しくお願い致します
容器の画像を添付致しました。
円形のPETボトルになります
販売先は自動車ディーラー様中心となります

ディーラー様及び通常の販売先において頂けるデザインでした
関係者で3点選びましたが、全員がこの方のデザインが上がりましたので
決定しました

沢山の方からデザインをあげて頂き非常に迷いました。
今後もこのサイトを使って新商品のデザインや
容器のデザインをお願いしたいと思いますのでその際は
宜しいお願い致します。今回はありがとうございました

```html
<!DOCTYPE html>
<html lang="ja">
<head>
<meta charset="utf-8">
<title>アルコール除菌ジェル ラベル</title>
<link rel="stylesheet" href="https://fonts.googleapis.com/css2?family=M+PLUS+Rounded+1c:wght@800&family=Noto+Sans+JP:wght@400;700&display=swap">
<style>
  :root{
    --bg:#c5e5f5;
    --label-top:#5fb3ea;
    --label-mid:#2a7cc8;
    --label-deep:#1a5aa3;
    --label-bottom:#1c4f95;
    --title-edge:#1d5fae;
    --ink:#ffffff;
    --rule:rgba(255,255,255,.55);
    --strip:#eef4f8;
  }
  *{box-sizing:border-box;margin:0;padding:0}
  html,body{width:1200px;height:1200px;overflow:hidden}
  body{background:var(--bg);font-family:"Noto Sans JP",sans-serif;color:var(--ink);position:relative}
  .label{
    position:absolute;left:220px;top:68px;width:760px;height:1064px;
    background:var(--label-bottom);overflow:hidden;
  }
  .label__strip{position:absolute;left:0;right:0;height:18px;background:var(--strip);z-index:2}
  .label__strip--top{top:0}
  .label__strip--bottom{bottom:0}
  .hero-art{
    position:absolute;left:0;top:18px;width:760px;height:500px;
    background:
      radial-gradient(ellipse 70% 18% at 55% 96%, rgba(255,255,255,.5), rgba(255,255,255,0) 70%),
      linear-gradient(180deg,var(--label-top) 0%,var(--label-mid) 60%,var(--label-deep) 100%);
  }
  .lower-band{
    position:absolute;left:0;top:518px;width:760px;height:528px;
    background:linear-gradient(180deg,var(--label-deep),var(--label-bottom));
  }
  .product-title{
    position:absolute;left:0;right:0;top:150px;text-align:center;
    font-family:"M PLUS Rounded 1c",sans-serif;font-weight:800;
    font-size:104px;line-height:1.15;letter-spacing:4px;color:var(--ink);
    -webkit-text-stroke:6px var(--title-edge);paint-order:stroke fill;
  }
  .label-body{
    position:absolute;left:40px;top:486px;width:680px;bottom:36px;
    display:flex;flex-direction:column;gap:22px;
  }
  .spec-row{display:flex;align-items:center;gap:14px}
  .spec-tag{border:2px solid var(--ink);padding:2px 10px;font-weight:700;font-size:24px;line-height:1.2}
  .spec-note{font-size:17px}
  .ingredients{width:100%;table-layout:fixed;border-collapse:collapse;font-size:12.5px;line-height:1.45}
  .ingredients th,.ingredients td{border-top:1px solid var(--rule);border-bottom:1px solid var(--rule);padding:4px 6px;text-align:left;vertical-align:top;font-weight:400}
  .ingredients .col-head{width:66px}
  .ingredients .col-main{width:262px}
  .ingredients .col-head2{width:76px}
  .ingredients th{letter-spacing:3px;white-space:nowrap}
  .ingredients td.split{border-right:1px solid var(--rule)}
  .cautions{font-size:12px;line-height:1.6}
  .cautions h3{font-size:12.5px;font-weight:700}
  .makers{margin-top:auto;font-size:13px;line-height:1.5}
  .makers p+p{margin-top:14px}
  .makers small{display:block;font-size:10px;opacity:.85}
  .recycle-marks{position:absolute;right:40px;bottom:60px;display:flex;gap:18px}
  .recycle-marks span{display:block;width:36px;height:36px;border:2px solid var(--ink);border-radius:50%}
</style>
</head>
<body>
  <main class="label">
    <div class="label__strip label__strip--top"></div>
    <div class="hero-art" role="img" aria-label="水の波と泡が浮かぶ青いイメージ"></div>
    <div class="lower-band"></div>

    <h1 class="product-title">アルコール<br>除菌ジェル</h1>

    <div class="label-body">
      <div class="spec-row">
        <span class="spec-tag">1L</span>
        <span class="spec-tag">火気厳禁</span>
        <span class="spec-note">(エタノール含有)</span>
      </div>

      <table class="ingredients">
        <colgroup><col class="col-head"><col class="col-main"><col class="col-head2"><col></colgroup>
        <tr><th>品名</th><td class="split">アルコール除菌ジェル</td><th>性状</th><td>無色のわずかに粘稠した液体です。</td></tr>
        <tr><th>成分</th><td class="split">エタノール(C2H6O)72.0~77.0vol%</td><th>用途</th><td>手指・皮膚の洗浄・消毒</td></tr>
        <tr><th>添加物</th><td class="split">グリセリン,カルボキシビニルポリマー,トリエタノールアミン</td><th>使用方法</th><td>適量を手のひらにとり、手指全体に伸ばし、乾燥するまで擦り込んでください。</td></tr>
      </table>

      <section class="cautions">
        <h3>使用上の注意</h3>
        <p>●次の人は使用しないでください。(1)損傷が広範囲の人 (2)深い傷やひどいやけどの人 ●目に入らないように注意してください。万一入った場合には、すぐに水またはぬるま湯で洗ってください。●外用にのみ使用してください。●使用後は手を十分に乾燥させてください。</p>
        <h3>保管及び取扱い上の注意</h3>
        <p>●直射日光の当たらない涼しい所に保管してください。●小児の手の届かない所に保管してください。●火気に近づけないでください。●家具・床・革製品などに付着しないようにしてください。</p>
        <p>【保管方法】容器を密閉し、火気を避けて室温保存。</p>
      </section>

      <div class="makers">
        <p>発売元：株式会社〇〇<small>※この表記はダミーです。この文章はダミーです。</small></p>
        <p>製造元：株式会社〇〇<small>※この表記はダミーです。この文章はダミーです。</small></p>
      </div>
    </div>

    <div class="recycle-marks" aria-hidden="true"><span></span><span></span></div>

    <div class="label__strip label__strip--bottom"></div>
  </main>
</body>
</html>
```